Velmar Industrial Coatings

We are looking to improve our business cards. Our company installs industrial floor and wall coatings in industrial, chemical and food processing plants.
Our coatings which consist of epoxy, urethane, and vinyl esters provide chemical and abrasion resistant surface with non-skid properties that are easy to clean.

Target Market(s)

food manufacturing, chemical plants, breweries and wineries, warehouses, clean room floors.

Industry/Entity Type

Construction

Contact Information for Business Card

improved current logo.

Colors

Designer to choose colors to be used in the design.

Requirements
Must have
• the information from uploaded file
Nice to have
• "We'll be outstanding on your floors."

```html
<!DOCTYPE html>
<html lang="en">
<head>
<meta charset="utf-8">
<title>Velmar Industrial Coatings – Business Card</title>
<link rel="stylesheet" href="https://fonts.googleapis.com/css2?family=Montserrat:wght@400;600;700&display=swap">
<style>
  :root {
    --backdrop: #2b211c;
    --card: #2d2d2f;
    --card-back: #2a2a2c;
    --green: #8aae3b;
    --white: #f2f2f2;
    --emboss: #3b3b3e;
  }
  * { margin: 0; padding: 0; box-sizing: border-box; }
  html, body { width: 1200px; height: 716px; overflow: hidden; }
  body {
    background: var(--backdrop);
    font-family: "Montserrat", sans-serif;
    display: flex;
    align-items: center;
    justify-content: center;
    gap: 48px;
  }
  .card {
    position: relative;
    width: 540px;
    height: 310px;
    border-radius: 4px;
    overflow: hidden;
    box-shadow: 0 10px 28px rgba(0,0,0,.45);
  }
  .card--front { background: var(--card); color: var(--white); }
  .card--back  { background: var(--card-back); display: flex; align-items: center; justify-content: center; }

  .holder-name {
    position: absolute; left: 34px; top: 40px;
    font-weight: 700; font-size: 19px; letter-spacing: .5px;
    color: var(--green); text-transform: uppercase;
  }
  .divider {
    position: absolute; left: 30px; right: 24px; top: 72px;
    height: 1px; background: var(--white);
  }
  .contact-list {
    position: absolute; left: 34px; top: 86px;
    list-style: none; font-size: 12.5px; line-height: 18px;
  }
  .contact-list li { display: flex; align-items: center; gap: 8px; }
  .contact-list svg { width: 10px; height: 10px; fill: var(--green); flex: none; }

  .company-name {
    position: absolute; right: 28px; top: 24px;
    font-weight: 700; font-size: 15px; letter-spacing: .3px;
    color: var(--white); text-transform: uppercase;
  }
  .address {
    position: absolute; right: 30px; bottom: 60px;
    text-align: right; font-size: 13px; line-height: 18px;
  }
  .footer-band { position: absolute; left: 0; bottom: 0; width: 100%; height: 60px; }
  .website {
    position: absolute; right: 30px; bottom: 10px;
    font-size: 13px; color: var(--white);
  }
  .back-name {
    font-weight: 700; font-size: 30px; letter-spacing: 1px;
    color: var(--emboss); text-transform: uppercase; text-align: center;
  }
</style>
</head>
<body>
  <section class="card card--front">
    <div class="holder-name">Reid Calloway</div>
    <div class="divider"></div>
    <ul class="contact-list">
      <li><svg viewBox="0 0 10 10"><path d="M2 0l2 2-1 1.5c.8 1.6 2 2.8 3.5 3.5L8 6l2 2-1.5 2C4 9.5.5 6 0 1.5z"/></svg>1-800-555-0142</li>
      <li><svg viewBox="0 0 10 10"><path d="M2 0l2 2-1 1.5c.8 1.6 2 2.8 3.5 3.5L8 6l2 2-1.5 2C4 9.5.5 6 0 1.5z"/></svg>(360) 555-0131</li>
      <li><svg viewBox="0 0 10 10"><rect x="1" y="3" width="8" height="6"/><rect x="3" y="0" width="4" height="3"/></svg>(360) 555-0133</li>
      <li><svg viewBox="0 0 10 10"><rect x="2.5" y="0" width="5" height="10" rx="1"/></svg>(360) 555-0117</li>
      <li><svg viewBox="0 0 10 10"><rect x="0" y="2" width="10" height="7"/></svg>reid@velmarfloors.com</li>
    </ul>
    <div class="company-name">Velmar Industrial Coatings Inc.</div>
    <address class="address" style="font-style:normal">Velmar Inc<br>Po Box 412<br>Harlow, Wa 98577</address>
    <svg class="footer-band" viewBox="0 0 540 60" preserveAspectRatio="none">
      <path d="M0 2 L185 28 L185 30 L0 5 Z" fill="#f2f2f2"/>
      <path d="M0 10 L180 35 Q190 26 205 27 L540 27 L540 60 L0 60 Z" fill="#8aae3b"/>
    </svg>
    <div class="website">www.velmarfloors.com</div>
  </section>

  <section class="card card--back">
    <div class="back-name">Velmar Industrial<br>Coatings Inc.</div>
  </section>
</body>
</html>
```